Boat Charter Power Point Template

Power Point Template for a Catalogue for a Boat Charter Company. In each slide there will be a main foto of the boat and then 3 mini photos plus all the aditional information of each boat. Here I attach 2 diferent presentations to get inspired

```html
<!DOCTYPE html>
<html lang="es">
<head>
<meta charset="utf-8">
<title>Boat Charter Template – Guía de uso</title>
<link href="https://fonts.googleapis.com/css2?family=Crimson+Pro:wght@400;500;600&family=Open+Sans:wght@400&family=Caladea&display=swap" rel="stylesheet">
<style>
  :root{
    --ink:#2f4a63;
    --ink-soft:#4a5d70;
    --rule:#7d8c99;
    --teal:#9fe0db;
    --teal-soft:#cdf1ee;
    --teal-deep:#7fd3cc;
    --sky:#e4f3fb;
    --note-orange:#e8792b;
    --note-green:#3f5a24;
    --note-blue:#4472c4;
    --note-ochre:#b8900a;
    --note-yellow:#f2c400;
    --photo-sea:#2f7fb5;
    --photo-sky:#bfe2f2;
  }
  *{box-sizing:border-box;margin:0;padding:0}
  html,body{width:1200px;height:2400px;overflow:hidden;background:#fff}
  body{position:relative;font-family:"Crimson Pro",Georgia,serif;color:var(--ink)}

  .note{position:absolute;font-family:"Open Sans",Arial,sans-serif;font-size:23px;line-height:32px}
  .note--images{left:65px;top:120px;width:230px;color:var(--note-orange)}
  .note--titles{left:323px;top:115px;width:380px;color:var(--note-green)}
  .note--table{left:804px;top:150px;width:305px;color:var(--note-blue);font-family:"Caladea",Cambria,serif;font-size:25px;line-height:32px}
  .note--icons{left:98px;top:915px;width:460px;color:var(--note-ochre)}
  .note--footer{left:662px;top:966px;width:460px;color:var(--note-green)}

  .guides{position:absolute;left:0;top:0;width:1200px;height:1100px;pointer-events:none;z-index:5}

  .slide{position:absolute;left:131px;width:944px;height:531px;overflow:hidden;background:#fff;
    box-shadow:6px 8px 14px rgba(0,0,0,.28)}
  .slide--one{top:352px}
  .slide--two{top:1216px}
  .slide--three{top:1830px;background:linear-gradient(180deg,var(--sky) 0%,#d7f1f4 60%,var(--teal-soft) 100%)}
  .slide__waves{position:absolute;inset:0;width:100%;height:100%}

  .slide__model,.slide__name{position:absolute;top:28px;font-size:38px;font-weight:500;letter-spacing:1px;color:var(--ink);line-height:48px}
  .slide__model{left:103px}
  .slide__name{left:384px;letter-spacing:2px}
  .slide--two .slide__name{left:382px}
  .slide__contact{position:absolute;left:787px;top:30px;font-size:17px;line-height:22px;color:var(--ink)}

  .photo{position:absolute;background:linear-gradient(180deg,var(--photo-sky) 0%,#8cc7df 35%,var(--photo-sea) 100%)}
  .photo--main{width:539px;height:288px;top:88px}
  .photo--mini{width:174px;height:109px;top:385px;background:linear-gradient(180deg,#3b86bd,#1f5f94)}
  .photo--interior{background:linear-gradient(180deg,#d9dcdc,#8a8f93)}
  .photo--cabin{background:linear-gradient(180deg,#2a2420,#b8956e)}

  .specs{position:absolute;width:313px;top:98px;font-size:9.5px;color:var(--ink-soft)}
  .slide--one .specs,.slide--three .specs{left:592px}
  .slide--two .specs{left:38px}
  .specs__title{text-align:center;font-size:13px;letter-spacing:3px;padding-bottom:4px;border-bottom:1px solid var(--rule)}
  .specs__grid{width:100%;border-collapse:collapse;text-align:center;margin-top:3px}
  .specs__grid td{height:20px;width:33.3%}
  .specs__cols{display:flex;justify-content:space-between;margin-top:12px}
  .specs__col{width:145px}
  .specs__col--inc{width:155px}
  .specs__head{text-align:center;font-size:12px;border-bottom:1px solid var(--rule);padding-bottom:2px;margin-bottom:3px}
  .list{list-style:none}
  .list li{height:20px;display:flex;align-items:center;white-space:nowrap}
  .list__qty{width:22px;padding-left:8px}
  .list__icon{width:16px;height:14px;margin:0 14px 0 4px;stroke:var(--ink-soft);fill:none;stroke-width:1.1;flex:none}
  .equip__head{text-align:center;font-size:12px;border-bottom:1px solid var(--rule);padding-bottom:2px;margin-top:6px}
  .equip__grid{display:grid;grid-template-columns:repeat(10,1fr);row-gap:5px;padding:6px 4px 0}
  .equip__grid svg{width:16px;height:15px;margin:auto;stroke:var(--ink-soft);fill:none;stroke-width:1.1}
  .terms{margin-top:12px;font-size:9.5px;line-height:13px;padding-left:2px}
  .terms u{font-weight:600}
</style>
</head>
<body>

<svg width="0" height="0" style="position:absolute" aria-hidden="true">
  <defs>
    <symbol id="i-person" viewBox="0 0 16 14"><circle cx="8" cy="4" r="2.6"/><path d="M3 13c0-3 2.2-5 5-5s5 2 5 5z"/></symbol>
    <symbol id="i-towel" viewBox="0 0 16 14"><rect x="3" y="1.5" width="10" height="11"/><path d="M3 4h10"/></symbol>
    <symbol id="i-drink" viewBox="0 0 16 14"><path d="M4 2h4l-1 11H5zM10 5h3v8h-3z"/></symbol>
    <symbol id="i-mask" viewBox="0 0 16 14"><rect x="2" y="4" width="10" height="6" rx="2"/><path d="M12 7h2V2"/></symbol>
    <symbol id="i-jetski" viewBox="0 0 16 14"><path d="M1 10h14l-3-3H5zM7 7l1-3"/></symbol>
    <symbol id="i-scooter" viewBox="0 0 16 14"><path d="M2 8c3-3 9-3 12 0-3 2-9 2-12 0z"/></symbol>
    <symbol id="i-board" viewBox="0 0 16 14"><rect x="5" y="1" width="5" height="12" rx="2.5"/><path d="M12 2v10"/></symbol>
    <symbol id="i-ac" viewBox="0 0 16 14"><rect x="1.5" y="3" width="13" height="5"/><path d="M4 10v2M8 10v2M12 10v2"/></symbol>
    <symbol id="i-gear" viewBox="0 0 16 14"><circle cx="8" cy="7" r="3"/><circle cx="8" cy="7" r="5.5"/></symbol>
    <symbol id="i-screen" viewBox="0 0 16 14"><rect x="2" y="2" width="12" height="8"/><path d="M6 12h4"/></symbol>
    <symbol id="i-umbrella" viewBox="0 0 16 14"><path d="M2 6a6 5 0 0 1 12 0zM8 6v7"/></symbol>
    <symbol id="i-box" viewBox="0 0 16 14"><rect x="3" y="2" width="10" height="10"/><circle cx="8" cy="7" r="1.2"/></symbol>
  </defs>
</svg>

<p class="note note--images">Soportes para imágenes puede cambiar o actualizar imágenes con un click</p>
<p class="note note--titles">Cuadros de texto que le permiten actualizar la información con facilidad ,&nbsp;&nbsp; las letras ajustan su tamaño dependiendo de la cantidad de información que se requiera mostrar</p>
<p class="note note--table">Tabla Insertada que permite actualizar la información fácilmente manteniendo el orden&nbsp; y la estética</p>
<p class="note note--icons">Se combinan Tablas Insertadas&nbsp; con soportes para imágenes<br>Lo que permite cambiar los iconos solo con dos click en el teclado</p>
<p class="note note--footer">Cuadros de texto que le permiten actualizar la información y ajustan el tamaño de las letras dependiendo de la cantidad de información que se requiera mostrar</p>

<!-- Slide one: annotated layout -->
<section class="slide slide--one">
  <svg class="slide__waves" viewBox="0 0 944 531" preserveAspectRatio="none" aria-hidden="true">
    <path d="M560 531 C640 440 780 330 944 250 L944 531Z" fill="var(--teal-soft)"/>
    <path d="M180 531 C420 480 620 470 760 380 C840 330 900 300 944 290 L944 531Z" fill="var(--teal)" opacity=".55"/>
    <path d="M600 531 C700 470 820 440 944 420 L944 531Z" fill="var(--teal-deep)" opacity=".5"/>
    <path d="M560 380 C700 340 820 250 944 210 L944 235 C820 275 700 365 560 395Z" fill="var(--teal)" opacity=".6"/>
  </svg>
  <h2 class="slide__model">Marlin&nbsp; 90</h2>
  <h2 class="slide__name">ELIA</h2>
  <p class="slide__contact">Lucía Moreno<br>+34 600 123 456</p>
  <div class="photo photo--main" style="left:9px" role="img" aria-label="Main photo of the yacht on turquoise water"></div>
  <div class="photo photo--mini" style="left:9px" role="img" aria-label="Aerial view of the yacht bow"></div>
  <div class="photo photo--mini" style="left:192px" role="img" aria-label="Sun deck with loungers"></div>
  <div class="photo photo--mini photo--interior" style="left:375px" role="img" aria-label="Covered aft deck seating"></div>
  <div class="specs">
    <div class="specs__title">Season&nbsp; €/day</div>
    <table class="specs__grid">
      <tr><td>High</td><td>Mid</td><td>Low</td></tr>
      <tr><td>9499</td><td>7899</td><td>7299</td></tr>
      <tr><td>Capacity</td><td>Fuel Cons</td><td>Lenght/Beam</td></tr>
      <tr><td>12+3 crew</td><td>600l/h 1350€</td><td>27m/6.5m</td></tr>
    </table>
    <div class="specs__cols">
      <div class="specs__col">
        <div class="specs__head">Accomodation</div>
        <ul class="list">
          <li><span class="list__qty">1</span>Master Cabin</li>
          <li><span class="list__qty">1</span>Vip Cabim</li>
          <li><span class="list__qty">1</span>1 Twin cabin</li>
          <li><span class="list__qty">3</span>Crew</li>
          <li><span class="list__qty">2</span>Crew cabins</li>
          <li><span class="list__qty">3</span>On suite Bathroom</li>
          <li><span class="list__qty">1</span>Crew Bathroom</li>
        </ul>
      </div>
      <div class="specs__col specs__col--inc">
        <div class="specs__head">Included</div>
        <ul class="list">
          <li><svg class="list__icon"><use href="#i-person"/></svg>Crew</li>
          <li><svg class="list__icon"><use href="#i-towel"/></svg>Towels</li>
          <li><svg class="list__icon"><use href="#i-drink"/></svg>Drinks /Snaks</li>
          <li><svg class="list__icon"><use href="#i-mask"/></svg>Snorkels</li>
          <li><svg class="list__icon"><use href="#i-jetski"/></svg>Wave Bike</li>
          <li><svg class="list__icon"><use href="#i-scooter"/></svg>Sea Scooter</li>
          <li><svg class="list__icon"><use href="#i-board"/></svg>Inflate /Paddle boards</li>
        </ul>
      </div>
    </div>
    <div class="equip__head">Equipment</div>
    <div class="equip__grid">
      <svg><use href="#i-ac"/></svg><svg><use href="#i-gear"/></svg><svg><use href="#i-screen"/></svg><svg><use href="#i-box"/></svg><svg><use href="#i-towel"/></svg><svg><use href="#i-box"/></svg><svg><use href="#i-board"/></svg><svg><use href="#i-drink"/></svg><svg><use href="#i-umbrella"/></svg><svg><use href="#i-gear"/></svg>
      <svg><use href="#i-screen"/></svg><svg><use href="#i-gear"/></svg><svg><use href="#i-umbrella"/></svg><svg><use href="#i-person"/></svg><svg><use href="#i-mask"/></svg><svg><use href="#i-jetski"/></svg><svg><use href="#i-ac"/></svg><svg><use href="#i-towel"/></svg><svg><use href="#i-drink"/></svg><svg><use href="#i-box"/></svg>
    </div>
    <p class="terms"><u>Includes:</u> 21% VAT, mooring in the base port, staff overtime, Mediterranean breakfast, bed linen and cleaning.<br><u>Not included:</u> Fuel, special orders (food, drinks, etc.), extra toys, chef, etc.</p>
  </div>
</section>

<!-- Slide two: mirrored layout -->
<section class="slide slide--two">
  <svg class="slide__waves" viewBox="0 0 944 531" preserveAspectRatio="none" aria-hidden="true">
    <path d="M0 210 C200 240 500 260 944 230 L944 250 C500 285 200 265 0 232Z" fill="var(--teal)" opacity=".6"/>
    <path d="M0 300 C250 330 600 340 944 300 L944 531 L0 531Z" fill="var(--teal-soft)"/>
    <path d="M0 380 C250 385 600 380 944 360 L944 531 L0 531Z" fill="var(--teal)" opacity=".5"/>
    <path d="M0 470 C120 500 200 520 260 531 L0 531Z" fill="#fff" opacity=".7"/>
    <path d="M300 531 C500 500 720 500 944 480 L944 531Z" fill="var(--teal-deep)" opacity=".45"/>
  </svg>
  <h2 class="slide__model">Solano&nbsp; 90</h2>
  <h2 class="slide__name">Blue Tempo</h2>
  <p class="slide__contact">Lucía Moreno<br>+34 600 123 456</p>
  <div class="photo photo--main" style="left:397px;background:linear-gradient(180deg,#1f5f94,#2f7fb5 60%,#3b8fc0)" role="img" aria-label="Main photo of the white yacht at sea"></div>
  <div class="photo photo--mini" style="left:397px" role="img" aria-label="Bow deck of the yacht"></div>
  <div class="photo photo--mini photo--interior" style="left:579px" role="img" aria-label="Saloon interior with sofas"></div>
  <div class="photo photo--mini photo--cabin" style="left:761px" role="img" aria-label="Master cabin bed"></div>
  <div class="specs">
    <div class="specs__title">Season&nbsp; €/day</div>
    <table class="specs__grid">
      <tr><td>High</td><td>Mid</td><td>Low</td></tr>
      <tr><td>9499</td><td>7899</td><td>7299</td></tr>
      <tr><td>Capacity</td><td>Fuel Cons</td><td>Lenght/Beam</td></tr>
      <tr><td>12+3 crew</td><td>600l/h 1350€</td><td>27.5 m/6.4m</td></tr>
    </table>
    <div class="specs__cols">
      <div class="specs__col">
        <div class="specs__head">Accomodation</div>
        <ul class="list">
          <li><span class="list__qty">3</span>Double Cabins</li>
          <li><span class="list__qty">1</span>Twin cabin</li>
          <li><span class="list__qty">1</span>Crew cabin</li>
          <li><span class="list__qty">4</span>On suite Bathroom</li>
          <li><span class="list__qty">2</span>Crew Bathroom</li>
        </ul>
      </div>
      <div class="specs__col specs__col--inc">
        <div class="specs__head">Included</div>
        <ul class="list">
          <li><svg class="list__icon"><use href="#i-person"/></svg>Crew</li>
          <li><svg class="list__icon"><use href="#i-towel"/></svg>Towels</li>
          <li><svg class="list__icon"><use href="#i-drink"/></svg>Drinks /Snaks</li>
          <li><svg class="list__icon"><use href="#i-mask"/></svg>Snorkels</li>
          <li><svg class="list__icon"><use href="#i-jetski"/></svg>Wave Bike (Tidera)</li>
          <li><svg class="list__icon"><use href="#i-scooter"/></svg>Sea Scooter</li>
          <li><svg class="list__icon"><use href="#i-board"/></svg>Inflate /Paddle boards (2)</li>
        </ul>
      </div>
    </div>
    <div class="equip__head">Equipment</div>
    <div class="equip__grid">
      <svg><use href="#i-ac"/></svg><svg><use href="#i-gear"/></svg><svg><use href="#i-screen"/></svg><svg><use href="#i-box"/></svg><svg><use href="#i-towel"/></svg><svg><use href="#i-box"/></svg><svg><use href="#i-board"/></svg><svg><use href="#i-drink"/></svg><svg><use href="#i-umbrella"/></svg><svg><use href="#i-gear"/></svg>
      <svg><use href="#i-screen"/></svg><svg><use href="#i-gear"/></svg><svg><use href="#i-umbrella"/></svg><svg><use href="#i-person"/></svg><svg><use href="#i-mask"/></svg><svg><use href="#i-jetski"/></svg><svg><use href="#i-ac"/></svg><svg><use href="#i-towel"/></svg><svg><use href="#i-drink"/></svg><svg><use href="#i-box"/></svg>
    </div>
    <p class="terms"><u>Includes:</u> 21% VAT, mooring in the base port, staff overtime, Mediterranean breakfast, bed linen and cleaning.<br><u>Not included:</u> Fuel, special orders (food, drinks, etc.), extra toys, chef, etc.</p>
  </div>
</section>

<!-- Slide three: blue background variant -->
<section class="slide slide--three">
  <svg class="slide__waves" viewBox="0 0 944 531" preserveAspectRatio="none" aria-hidden="true">
    <path d="M560 531 C680 430 800 340 944 280 L944 531Z" fill="var(--teal)" opacity=".45"/>
    <path d="M560 390 C700 350 820 270 944 230 L944 255 C820 295 700 375 560 405Z" fill="#fff" opacity=".5"/>
    <path d="M300 531 C500 500 700 480 944 440 L944 531Z" fill="var(--teal-deep)" opacity=".4"/>
  </svg>
  <h2 class="slide__model">Marlin&nbsp; 90</h2>
  <h2 class="slide__name">ELIA</h2>
  <p class="slide__contact">Lucía Moreno<br>+34 600 123 456</p>
  <div class="photo photo--main" style="left:9px" role="img" aria-label="Main photo of the yacht on turquoise water"></div>
  <div class="photo photo--mini" style="left:9px" role="img" aria-label="Aerial view of the yacht bow"></div>
  <div class="photo photo--mini" style="left:192px" role="img" aria-label="Sun deck with loungers"></div>
  <div class="photo photo--mini photo--interior" style="left:375px" role="img" aria-label="Covered aft deck seating"></div>
  <div class="specs">
    <div class="specs__title">Season&nbsp; €/day</div>
    <table class="specs__grid">
      <tr><td>High</td><td>Mid</td><td>Low</td></tr>
      <tr><td>9499</td><td>7899</td><td>7299</td></tr>
      <tr><td>Capacity</td><td>Fuel Cons</td><td>Lenght/Beam</td></tr>
      <tr><td>12+3 crew</td><td>600l/h 1350€</td><td>27m/6.5m</td></tr>
    </table>
    <div class="specs__cols">
      <div class="specs__col">
        <div class="specs__head">Accomodation</div>
        <ul class="list">
          <li><span class="list__qty">1</span>Master Cabin</li>
          <li><span class="list__qty">1</span>Vip Cabim</li>
          <li><span class="list__qty">1</span>1 Twin cabin</li>
          <li><span class="list__qty">3</span>Crew</li>
          <li><span class="list__qty">2</span>Crew cabins</li>
          <li><span class="list__qty">3</span>On suite Bathroom</li>
          <li><span class="list__qty">1</span>Crew Bathroom</li>
        </ul>
      </div>
      <div class="specs__col specs__col--inc">
        <div class="specs__head">Included</div>
        <ul class="list">
          <li><svg class="list__icon"><use href="#i-person"/></svg>Crew</li>
          <li><svg class="list__icon"><use href="#i-towel"/></svg>Towels</li>
          <li><svg class="list__icon"><use href="#i-drink"/></svg>Drinks /Snaks</li>
          <li><svg class="list__icon"><use href="#i-mask"/></svg>Snorkels</li>
          <li><svg class="list__icon"><use href="#i-jetski"/></svg>Wave Bike</li>
          <li><svg class="list__icon"><use href="#i-scooter"/></svg>Sea Scooter</li>
          <li><svg class="list__icon"><use href="#i-board"/></svg>Inflate /Paddle boards</li>
        </ul>
      </div>
    </div>
    <div class="equip__head">Equipment</div>
    <div class="equip__grid">
      <svg><use href="#i-ac"/></svg><svg><use href="#i-gear"/></svg><svg><use href="#i-screen"/></svg><svg><use href="#i-box"/></svg><svg><use href="#i-towel"/></svg><svg><use href="#i-box"/></svg><svg><use href="#i-board"/></svg><svg><use href="#i-drink"/></svg><svg><use href="#i-umbrella"/></svg><svg><use href="#i-gear"/></svg>
      <svg><use href="#i-screen"/></svg><svg><use href="#i-gear"/></svg><svg><use href="#i-umbrella"/></svg><svg><use href="#i-person"/></svg><svg><use href="#i-mask"/></svg><svg><use href="#i-jetski"/></svg><svg><use href="#i-ac"/></svg><svg><use href="#i-towel"/></svg><svg><use href="#i-drink"/></svg><svg><use href="#i-box"/></svg>
    </div>
    <p class="terms"><u>Includes:</u> 21% VAT, mooring in the base port, staff overtime, Mediterranean breakfast, bed linen and cleaning.<br><u>Not included:</u> Fuel, special orders (food, drinks, etc.), extra toys, chef, etc.</p>
  </div>
</section>

<!-- Callout lines and highlight ellipses -->
<svg class="guides" viewBox="0 0 1200 1100" aria-hidden="true" fill="none" stroke-width="2">
  <g stroke="var(--note-orange)">
    <path d="M178 319 L239 619 M178 319 L197 778 M178 319 L384 806 M178 319 L623 788 M178 319 L403 553"/>
  </g>
  <g stroke="var(--note-green)">
    <path d="M338 377 L511 314 L548 377"/>
    <ellipse cx="331" cy="403" rx="133" ry="24"/>
    <ellipse cx="553" cy="403" rx="78" ry="24"/>
    <ellipse cx="884" cy="823" rx="190" ry="28"/>
    <path d="M858 851 L858 956 L895 956"/>
  </g>
  <g stroke="var(--note-blue)">
    <path d="M783 232 L711 232 L806 427 M711 232 L727 563"/>
    <ellipse cx="870" cy="494" rx="184" ry="54"/>
    <ellipse cx="780" cy="645" rx="80" ry="103"/>
  </g>
  <g stroke="var(--note-ochre)">
    <path d="M533 966 L609 964 L856 667"/>
    <ellipse cx="897" cy="645" rx="39" ry="75"/>
    <ellipse cx="873" cy="766" rx="181" ry="28"/>
  </g>
  <path d="M609 964 L816 802" stroke="var(--note-yellow)"/>
</svg>

</body>
</html>
```